Snapframe Party Rentals New Business Card*

Need a business card designed for a Photo Booth Hire company.Must look very professional and colorful.A new creative logo would be a bonus. Our current logo is attached on here.

Contact Information for Business Card

Business Name: SNAPFRAME PARTY RENTALS
Contact Person: MARCUS OKAFOR
Mobile: 0491826350
Email: INFO@SNAPFRAMERENTALS.EXAMPLE
Website: WWW.SNAPFRAMERENTALS.EXAMPLE
Facebook: WWW.FACEBOOK.COM/SNAPFRAME.PARTY.RNT

Font styles to use
Serif
Sans Serif
Script

Colors

Designer to choose colors to be used in the design.

Requirements
Must have
• Bonus if the colors match our website.

```html
<!DOCTYPE html>
<html lang="en">
<head>
<meta charset="UTF-8">
<title>Snapframe Party Rentals – Business Card</title>
<link href="https://fonts.googleapis.com/css2?family=Montserrat:wght@400;500;600;700&display=swap" rel="stylesheet">
<style>
  :root {
    --stage: #2a2a2c;
    --card: #1f2021;
    --card-edge: #2b2c2d;
    --ink: #f4f4f4;
    --ink-soft: #d9d9d9;
    --silver: #c9c9c9;
  }
  * { margin: 0; padding: 0; box-sizing: border-box; }
  html, body { width: 1200px; height: 800px; overflow: hidden; }
  body {
    background: var(--stage);
    font-family: "Montserrat", Arial, sans-serif;
    color: var(--ink);
    position: relative;
  }
  .card {
    position: absolute;
    top: 245px;
    width: 540px;
    height: 309px;
    background: var(--card);
    border: 1px solid var(--card-edge);
    border-radius: 4px;
    box-shadow: 0 18px 40px rgba(0,0,0,0.45);
  }
  .card--front { left: 40px; }
  .card--back { left: 620px; }

  /* Front */
  .front-mark {
    position: absolute;
    left: 0; right: 0; top: 92px;
    display: flex; align-items: center; justify-content: center; gap: 12px;
  }
  .front-mark__dot {
    width: 18px; height: 18px; border-radius: 50%;
    background: var(--silver);
  }
  .front-mark__name {
    font-weight: 700; font-size: 26px; letter-spacing: 1px;
    color: var(--silver);
  }
  .front-url {
    position: absolute; left: 0; right: 0; top: 196px;
    text-align: center;
    font-weight: 600; font-size: 14px; letter-spacing: 0.5px;
    color: var(--ink);
  }

  /* Back */
  .brand {
    position: absolute; right: 36px; top: 44px;
    text-align: right;
  }
  .brand__name {
    font-weight: 700; font-size: 22px; line-height: 1.05;
    color: var(--ink);
  }
  .brand__url {
    margin-top: 4px;
    font-weight: 600; font-size: 8.5px; letter-spacing: 0.3px;
    color: var(--ink);
  }
  .contact {
    position: absolute; left: 36px; bottom: 34px;
  }
  .contact__name {
    font-weight: 700; font-size: 19px; letter-spacing: 1px;
    margin-bottom: 12px;
  }
  .contact__list { list-style: none; }
  .contact__item {
    display: flex; align-items: center; gap: 9px;
    font-weight: 400; font-size: 12px; letter-spacing: 0.4px;
    color: var(--ink-soft);
    line-height: 1.7;
  }
  .contact__icon { width: 11px; height: 11px; flex: none; }
</style>
</head>
<body>

<section class="card card--front" aria-label="Business card front">
  <div class="front-mark">
    <span class="front-mark__dot"></span>
    <span class="front-mark__name">SNAPFRAME PARTY RENTALS</span>
  </div>
  <p class="front-url">WWW.SNAPFRAMERENTALS.EXAMPLE</p>
</section>

<section class="card card--back" aria-label="Business card back">
  <div class="brand">
    <p class="brand__name">SNAPFRAME<br>PARTY RENTALS</p>
    <p class="brand__url">WWW.SNAPFRAMERENTALS.EXAMPLE</p>
  </div>

  <div class="contact">
    <p class="contact__name">MARCUS OKAFOR</p>
    <ul class="contact__list">
      <li class="contact__item">
        <svg class="contact__icon" viewBox="0 0 12 12"><rect x="2.5" y="0.8" width="7" height="10.4" rx="1.2" fill="none" stroke="#f4f4f4" stroke-width="1.2"/><line x1="5" y1="9.3" x2="7" y2="9.3" stroke="#f4f4f4" stroke-width="1"/></svg>
        0491826350
      </li>
      <li class="contact__item">
        <svg class="contact__icon" viewBox="0 0 12 12"><rect x="0.8" y="2.2" width="10.4" height="7.6" fill="#f4f4f4"/><polyline points="0.8,2.4 6,6.6 11.2,2.4" fill="none" stroke="#1f2021" stroke-width="1.1"/></svg>
        INFO@SNAPFRAMERENTALS.EXAMPLE
      </li>
      <li class="contact__item">
        <svg class="contact__icon" viewBox="0 0 12 12"><circle cx="6" cy="6" r="5.2" fill="none" stroke="#f4f4f4" stroke-width="1.1"/><ellipse cx="6" cy="6" rx="2.2" ry="5.2" fill="none" stroke="#f4f4f4" stroke-width="0.9"/><line x1="0.8" y1="6" x2="11.2" y2="6" stroke="#f4f4f4" stroke-width="0.9"/></svg>
        WWW.SNAPFRAMERENTALS.EXAMPLE
      </li>
      <li class="contact__item">
        <svg class="contact__icon" viewBox="0 0 12 12"><circle cx="6" cy="6" r="5" fill="#f4f4f4"/></svg>
        WWW.SOCIALPAGE.EXAMPLE/SNAPFRAME.PARTY
      </li>
    </ul>
  </div>
</section>

</body>
</html>
```